TAVRO Capital Group LLC a High Risk Big Rewards company for Rich Young Entrepreneurs

We would like a very modern, powerful in the eyes of our customers, modern, minimalist feel, financial gain. this business card is for young Rich entrepreneurs who want to invest money into High Risk, Big Rewards Businesses. The card Should sell the business!! let your creativity go Wild! I pick most of the designers for this project because of your BOLD Designs, I would like this card to be Bold, Modern, Minimalist, use as many effects in your graphic Artist Mind, Do not let the Financial sound of this business to make you think Conservative that's the last thing we are! if you have a lot of money and you want to play a risky market call US
Updates

Project Deadline Extended
Reason: have not received, enough designs to choose 1st and second place, sure I have received over 100 designs but it seems most designers are submitting every card they have ever made before and calling it mine, please we are looking for fresh ideas please!

Target Market(s)

Private Risky Investors

Industry/Entity Type

Financial

Contact Information for Business Card

powerful in the eyes of our customers,modern, minimalist feel

Font styles to use
Other font styles liked:
• Modern feeling fonts

Requirements
Must have
• The Company Name is TAVRO Capital Group LLC and it must be on the CARD
• My Name, title, Cell , email
• Delvin Ashcroft G.E.D.
• Managing Member
• 555.038.6195
• delvin@tavrocapitalgroup.example
Nice to have
• try a black thick plastic card with round corners with Delvin Ashcroft GED (make sure GED is smaller than name) just on one side of the card, and my phone number with out the icons and email on the other side, this card should look like a exclusive credit card or exclusive VIP card, something you would never loose

```html
<!DOCTYPE html>
<html lang="en">
<head>
<meta charset="UTF-8">
<title>TAVRO Capital Group LLC – Business Card</title>
<link rel="stylesheet" href="https://fonts.googleapis.com/css2?family=Jost:wght@300;600&family=Source+Sans+3:wght@400;700&display=swap">
<style>
  :root {
    --page-bg: #ececec;
    --card-light: #6b6b6b;
    --card-mid: #4a4a4a;
    --card-dark: #262626;
    --ink: #e4e4e4;
    --ink-soft: #d2d2d2;
  }
  * { margin: 0; padding: 0; box-sizing: border-box; }
  html, body {
    width: 1200px;
    height: 720px;
    overflow: hidden;
    background: var(--page-bg);
  }
  .canvas {
    position: relative;
    width: 1200px;
    height: 720px;
  }
  .card {
    position: absolute;
    width: 525px;
    height: 300px;
    border-radius: 4px;
    overflow: hidden;
    color: var(--ink);
  }
  .card--front {
    left: 60px;
    top: 60px;
    background: linear-gradient(160deg, var(--card-light) 0%, var(--card-mid) 55%, var(--card-dark) 100%);
  }
  .card--back {
    left: 615px;
    top: 360px;
    background: linear-gradient(200deg, var(--card-light) 0%, var(--card-mid) 45%, var(--card-dark) 100%);
  }

  /* Front */
  .brand {
    position: absolute;
    left: 56px;
    top: 52px;
  }
  .brand__name {
    font-family: 'Jost', sans-serif;
    font-weight: 600;
    font-size: 104px;
    line-height: 0.9;
    letter-spacing: -1px;
    color: var(--ink);
  }
  .brand__descriptor {
    margin-top: 14px;
    font-family: 'Jost', sans-serif;
    font-weight: 300;
    font-size: 36px;
    line-height: 1.1;
    color: var(--ink);
  }

  /* Back */
  .brand-strip {
    position: absolute;
    left: -8px;
    top: 0;
    width: 120px;
    height: 300px;
    overflow: hidden;
  }
  .brand-strip__name {
    position: absolute;
    left: 10px;
    bottom: -30px;
    transform-origin: left bottom;
    transform: rotate(-90deg) translateY(100%);
    font-family: 'Jost', sans-serif;
    font-weight: 600;
    font-size: 118px;
    line-height: 1;
    white-space: nowrap;
    color: var(--ink);
  }
  .contact {
    position: absolute;
    left: 170px;
    top: 30px;
    font-family: 'Source Sans 3', sans-serif;
    color: var(--ink-soft);
  }
  .contact__name {
    font-weight: 700;
    font-size: 23px;
    line-height: 1.1;
    color: var(--ink);
  }
  .contact__credential {
    font-size: 10px;
    font-weight: 700;
    vertical-align: super;
    margin-left: 2px;
  }
  .contact__title {
    font-weight: 700;
    font-size: 18px;
    line-height: 1.2;
    color: var(--ink);
  }
  .contact__details {
    list-style: none;
    margin-top: 16px;
    font-size: 15.5px;
    line-height: 1.32;
  }
  .contact__web {
    margin-top: 14px;
    font-size: 15.5px;
  }
</style>
</head>
<body>
<main class="canvas">
  <section class="card card--front" aria-label="Business card front">
    <div class="brand">
      <div class="brand__name">TAVRO</div>
      <div class="brand__descriptor">Capital Group LLC</div>
    </div>
  </section>

  <section class="card card--back" aria-label="Business card back">
    <div class="brand-strip" aria-hidden="true">
      <span class="brand-strip__name">TAVRO</span>
    </div>
    <div class="contact">
      <p class="contact__name">Delvin Ashcroft<span class="contact__credential">G.E.D.</span></p>
      <p class="contact__title">Managing Member</p>
      <ul class="contact__details">
        <li>Address line 1</li>
        <li>Address line 2</li>
        <li>phone: 555.038.6195</li>
        <li>mobile: 555.038.6195</li>
        <li>email:</li>
        <li>delvin@tavrocapitalgroup.example</li>
      </ul>
      <p class="contact__web">www.tavro.example</p>
    </div>
  </section>
</main>
</body>
</html>
```